Marketing / Informational Site for Marriage and Family Therapists Cooperative

We need a web design for a new Marriage and Family Therapist Cooperative, called Meadowgate Counselors. This is a market and information site for potential clients and referrals to learn more about the team and get contact information.

We are looking for profession, clean, and modern design, that cater towards families and mom's concerned about their families mental health and child development.

This should include a home page, an general about page, 3 bio pages (1 for each therapist listed below), and a general contact us page.

Our Domain Name

Meadowgatecounselors.example

Company Name

Meadowgate Counselors

Group Moto/Philosophy

“Our sorrows and wounds are healed only when we touch them with compassion.” - Orvelan

Our Logo

See Heron Final (attached)

Home Page (Introduction)

Feeling stressed and overwhelmed?
Encountering barriers towards your goals?
Having difficulty accomplishing the simplest task?
Have the need to talk but unsure who to turn to?

Therapy can assist you in overcoming all of these challenges. Assist you in uncovering the difficulties and barriers that are keeping you from achieving your life’s ambitions, help discover ways to overcome them, and cope with the impact your behaviour has on your occupation, personal life and social life.

Welcome to our practice, with over 20 years of combined experience in the clinical field you are sure to find the right fit for your needs. Each clinician has experience working with groups, adults, teens, children, families, and couples. We specialize in fostering healthy relationships between individuals, managing depression and anxiety, overcoming trauma, and developing occupational success. Feel free to explore information about each clinician and make an appointment with one of us today.

About Us (bio pics attached)

Marisel Dunkworth

My name is Dr. MariSel Dunkworth and I am a Licensed Marriage Family Therapist with a practice in Riverside, CA. I have devoted my life’s work into developing my skills in this profession. I have over 15 years of experience working in the clinical and the social service settings. These years have afforded me the opportunity to work with groups, families, adults, teens and children with varying symptoms. I have helped clients that have trauma, abuse histories, and many within the legal or social service systems. I enjoy working individuals from all walks of life achieve self sufficiency, social success and occupational success. In my years of training I have come to develop a culturally sensitive practice that centers around the needs of the client.

I have held many positions in my clinical career beginning as clinician moving upwards toward supervisor and program coordinator. I have also over 5 years of experience as an adjunct faculty member in the University setting teaching student to become Marriage and Family Therapists. As a clinician I focused on enriching my clinical skills by developing outcome driven practices to achieve client’s desired goals. As a clinical supervisor, I guided clinicians along their own paths towards clinical licensure. As a program coordinator, I helped develop a clinical assessment and triage program from ground up to assist client in accessing services in the South Los Angeles Area. The program would assist over 100 plus clients on a monthly basis get connected to clinical services and linked to any additional resources as needed by the individual. I have graduated with my, Bachelor’s degree at the Halvern College, Riverside. I received my Masters degree in Clinical Psychology at Mount St. Mary’s University, and my Doctorate degree in Clinical Psychology at Tamsworth Institute.

To schedule an appointment with Dr. MariSel Dunkworth, LMFT:

email: marisel582@postbox.example
Phone: (951)555-0182

Jeb Kowal

My name is Rosalindra (Jeb) Kowal, I received my Masters Degree of Counseling in Marriage and Family Therapy from Corvell Bay State College in June 2000. I have acquired over 15 years of experience helping Individuals, Couples, and Families cope with issues of Anxiety, Depression, Grief and Bereavement, and HIV/AIDS.

I am a Family Systems Therapist and I truly believe the dynamics in our family of origin greatly shape our current belief systems and behaviors. However, I often utilize a variety of approaches to help my clients achieve their goals depending on their individual needs.

My greatest strength as a Marriage and Family Therapist is helping my clients explore ways to make the changes in their lives that will allow them to live their life to their fullest potential. I help my clients achieve their personal life goals with a warm, safe, non-judgmental , and supportive environment. In doing so, my clients are encouraged to explore the issues that may be preventing them from living the life they desire. Thus, empowering them to take control of their personal journey to living a productive and meaningful life.

If you feel that you are ready to commit to bringing about positive changes in your life and would like support in exploring this path, I’m here to work with you in your journey to personal growth and development.

To schedule an appointment with Rosalindra Kowal, LMFT:

e-mail: rkjeb7@mailnest.example
Phone: (951)555-0147

Dena Holcroft

Dena Holcroft graduated with a Masters in Marriage and Family Therapy from Pellridge Crestwood College. She currently holds a license in Marriage and Family Therapy in the State of California. She is also formally trained in Clinical Art Therapy. Dena's expertise lies in providing treatment to individuals experiencing work-related injuries, severe physical and emotional pain, trauma, grief and loss, anxiety and depression. In her early career, she provided valuable service at the largest free clinic in the nation serving marginalized families and children. For the past ten years, Dena has worked with HIV/AIDS population.
Dena comes from a multicultural background and she has utilized this experience and knowledge in serving a variety of populations. At an organizational level, Dena has worked extensively with challenging issues such as the chemical dependency and homelessness. In her private practice, Dena is proficient in working within individuals experiencing relationship concerns, marital and family conflict, depression/anxiety, self-esteem concerns, adjustment disorders, and pain management. She has treated clients from diverse cultural, linguistic backgrounds and sexual orientations.
Dena is trained in Family Systems Theory and incorporates other strategies appropriate for each presenting issue. She specializes in Clinical Art Therapy and has successfully utilized an integrated approach including guided imagery and relaxation skills training for many years.

To schedule an appointment with Dena Holcroft, LMFT

e-mail: greypinestudio@inkmail.example
Phone: (951) 555-0169

Target Market(s)

Families with child development, marriage issues, or other mental health needs

Industry/Entity Type

Marketing

Number of Pages Required

5+ page

Requirements
Must have
• 1 home page, 1 about page, 1 contact page. About page could either be standalone page with 3 different bio pages for each therapist or an all in one about page that includes bios for all 3 therapists.

```html
<!DOCTYPE html>
<html lang="en">
<head>
<meta charset="utf-8">
<title>Meadowgate Counselors</title>
<link href="https://fonts.googleapis.com/css2?family=Open+Sans:wght@300;400;600;700&display=swap" rel="stylesheet">
<style>
:root{
  --green:#b9cf5c;
  --green-dark:#9fb842;
  --green-light:#cfe08a;
  --teal:#a8d2d6;
  --ink:#333;
  --muted:#777;
  --grey:#b5b5b5;
  --white:#fff;
}
*{box-sizing:border-box;margin:0;padding:0}
html,body{width:1200px;height:2356px;overflow:hidden}
body{font-family:"Open Sans",Arial,sans-serif;color:var(--ink);background:var(--white);position:relative}
.topbar{height:160px;position:relative}
.social{position:absolute;left:40px;top:62px;display:flex;gap:8px}
.social span{width:28px;height:28px;border-radius:50%;background:var(--grey);display:block}
.brand{position:absolute;left:0;right:0;top:40px;text-align:center}
.brand .mark{width:56px;height:56px;border-radius:50%;background:var(--green);margin:0 auto 10px}
.brand .name{font-size:20px;font-weight:600;color:var(--muted);letter-spacing:1px}
.account{position:absolute;right:40px;top:64px;display:flex;gap:12px}
.account a{font-size:11px;color:#fff;text-decoration:none;padding:7px 16px;letter-spacing:1px}
.account .login{background:var(--teal)}
.account .signup{background:var(--green)}
.hero{position:absolute;top:160px;left:0;width:1200px;height:620px;background:radial-gradient(circle at 25% 40%,#eef6c8 0,#cfe48a 40%,#a9c84e 100%)}
.hero .photo{position:absolute;right:120px;top:60px;width:360px;height:560px;background:linear-gradient(180deg,#d9e4ef,#7a93c4);border-radius:6px 6px 0 0}
.nav{position:absolute;top:180px;left:100px;width:1000px;height:46px;background:var(--green-light);display:flex;align-items:center;padding:0 20px;z-index:2}
.nav a{color:#fff;font-size:12px;text-decoration:none;letter-spacing:1px;width:160px;text-align:center}
.nav .home{background:var(--green);height:46px;line-height:46px}
.nav .search{margin-left:auto;width:220px;height:26px;background:#fff;font-size:11px;color:#aaa;padding:5px 10px}
.hero-text{position:absolute;left:40px;top:250px;width:560px;color:#fff}
.hero-text h1{font-size:72px;font-weight:300;letter-spacing:2px}
.hero-text p{font-size:22px;line-height:1.35;margin-top:10px}
.hero-text a{display:inline-block;margin-top:18px;color:#fff;font-size:14px}
.arrow{position:absolute;top:470px;width:14px;height:24px;z-index:2}
.arrow.left{left:30px}.arrow.right{right:30px}
.welcome{position:absolute;top:800px;left:0;width:1200px;text-align:center}
h2{font-size:38px;font-weight:400;letter-spacing:1px}
.welcome p{width:860px;margin:26px auto 0;font-size:12px;line-height:1.7;color:var(--muted)}
.focus{display:flex;justify-content:center;gap:90px;margin-top:34px}
.focus div{width:140px;font-size:12px;font-weight:700}
.focus .icon{width:100px;height:100px;border-radius:50%;background:var(--green);margin:0 auto 18px;display:flex;align-items:center;justify-content:center}
.about{position:absolute;top:1200px;left:0;width:1200px;height:320px;background:var(--teal);text-align:center;color:#fff}
.about h2{padding-top:50px}
.about p{width:880px;margin:24px auto 0;font-size:13px;line-height:1.7}
.about a{display:inline-block;margin-top:30px;background:var(--green);color:#fff;text-decoration:none;font-size:12px;padding:12px 26px;letter-spacing:1px}
.services{position:absolute;top:1545px;left:0;width:1200px;text-align:center}
.cards{display:flex;gap:28px;justify-content:center;margin-top:40px;text-align:left}
.card{width:232px}
.card .photo{height:160px;border-radius:2px}
.card h3{font-size:13px;font-weight:700;margin-top:22px;line-height:1.4}
.card p{font-size:11px;color:var(--muted);line-height:1.6;margin-top:10px}
.card a{display:block;font-size:11px;color:var(--green-dark);margin-top:8px}
.footer{position:absolute;top:2040px;left:0;width:1200px;height:316px;background:var(--green);color:#fff}
.footer .col{position:absolute;top:44px}
.f-brand{left:90px;width:260px}
.f-brand .mark{width:48px;height:48px;border-radius:50%;background:#fff;opacity:.8}
.f-brand .name{font-size:18px;font-weight:600;margin-top:10px}
.f-brand p{font-size:11px;line-height:1.6;margin-top:16px}
.footer h4{font-size:14px;font-weight:600;letter-spacing:1px}
.f-news{left:450px;width:320px}
.f-news p{font-size:11px;margin-top:16px;line-height:1.6}
.f-news .input{margin-top:14px;width:280px;height:30px;background:#fff;color:#aaa;font-size:11px;padding:7px 10px}
.f-news .btn{margin-top:10px;display:inline-block;background:var(--teal);font-size:11px;padding:7px 16px}
.f-contact{left:820px;width:300px}
.f-contact ul{list-style:none;margin-top:16px}
.f-contact li{font-size:11px;line-height:1.6;margin-bottom:12px;display:flex;gap:10px}
.f-contact svg{flex:none;margin-top:2px}
.copyright{position:absolute;bottom:22px;left:0;right:0;text-align:center;font-size:11px}
</style>
</head>
<body>
<header class="topbar">
  <div class="social"><span></span><span></span><span></span><span></span><span></span></div>
  <div class="brand"><div class="mark"></div><div class="name">Meadowgate Counselors</div></div>
  <div class="account"><a class="login" href="#">LOGIN</a><a class="signup" href="#">SIGN UP</a></div>
</header>

<section class="hero">
  <div class="photo" role="img" aria-label="Photo of a smiling therapist in a blue shirt, arms crossed"></div>
</section>
<nav class="nav">
  <a class="home" href="#">HOME</a><a href="#">ABOUT US</a><a href="#">OUR TEAM</a><a href="#">CONTACT US</a>
  <div class="search">SEARCH</div>
</nav>
<svg class="arrow left" viewBox="0 0 14 24"><path d="M12 2 2 12l10 10" fill="none" stroke="#fff" stroke-width="3"/></svg>
<svg class="arrow right" viewBox="0 0 14 24"><path d="M2 2l10 10L2 22" fill="none" stroke="#fff" stroke-width="3"/></svg>
<div class="hero-text">
  <h1>LMFT</h1>
  <p>Our sorrows and wounds are healed only when we touch them with compassion.</p>
  <a href="#">Read more</a>
</div>

<section class="welcome">
  <h2>WELCOME TO LMFT</h2>
  <p>Welcome to our practice, with over 20 years of combined experience in the clinical field you are sure to find the right fit for your needs. Each clinician has experience working with groups, adults, teens, children, families, and couples. We specialize in fostering healthy relationships between individuals, managing depression and anxiety, overcoming trauma, and developing occupational success.</p>
  <div class="focus">
    <div><span class="icon"><svg width="44" height="44" viewBox="0 0 44 44" fill="none" stroke="#fff" stroke-width="3"><circle cx="22" cy="15" r="8"/><path d="M8 40c0-9 6-14 14-14s14 5 14 14"/></svg></span>INDIVIDUALS</div>
    <div><span class="icon"><svg width="44" height="44" viewBox="0 0 44 44" fill="none" stroke="#fff" stroke-width="3"><circle cx="22" cy="22" r="18"/><circle cx="16" cy="18" r="1.5" fill="#fff"/><circle cx="28" cy="18" r="1.5" fill="#fff"/><path d="M14 31c4-4 12-4 16 0"/></svg></span>DEPRESSION AND ANXIETY</div>
    <div><span class="icon"><svg width="44" height="44" viewBox="0 0 44 44" fill="none" stroke="#fff" stroke-width="3"><circle cx="22" cy="22" r="18"/><path d="M22 22l8-8M22 10v3"/></svg></span>OVERCOMING TRAUMA</div>
    <div><span class="icon"><svg width="44" height="44" viewBox="0 0 44 44" fill="none" stroke="#fff" stroke-width="3"><path d="M6 20h7v18H6zM13 22l8-14c3 0 4 2 3 6l-1 4h11c2 0 3 2 2 4l-4 14H13"/></svg></span>OCCUPATIONAL SUCCESS</div>
  </div>
</section>

<section class="about">
  <h2>ABOUT US</h2>
  <p>Therapy can assist you in overcoming all of these challenges. Assist you in uncovering the difficulties and barriers that are keeping you from achieving your life’s ambitions, help discover ways to overcome them, and cope with the impact your behaviour has on your occupation, personal life and social life.</p>
  <a href="#">BOOK AN APPOINTMENT</a>
</section>

<section class="services">
  <h2>OUR SERVICES</h2>
  <div class="cards">
    <article class="card"><div class="photo" role="img" aria-label="Photo of a counselling session with an individual client" style="background:linear-gradient(135deg,#e8e2d8,#8a9aa8)"></div><h3>FEELING STRESSED AND OVERWHELMED?</h3><p>Therapy can assist you in overcoming all of these challenges. Assist you in uncovering the difficulties.</p><a href="#">Read more</a></article>
    <article class="card"><div class="photo" role="img" aria-label="Photo of a smiling family together at home" style="background:linear-gradient(135deg,#cfe3ef,#5f86a8)"></div><h3>ENCOUNTERING BARRIERS TOWARDS YOUR GOALS?</h3><p>Therapy can assist you in overcoming all of these challenges. Assist you in uncovering the difficulties.</p><a href="#">Read more</a></article>
    <article class="card"><div class="photo" role="img" aria-label="Photo of a couple talking with a therapist" style="background:linear-gradient(135deg,#f0e6dc,#b0574f)"></div><h3>HAVING DIFFICULTY ACCOMPLISH THE SIMPLEST TASK?</h3><p>Therapy can assist you in overcoming all of these challenges. Assist you in uncovering the difficulties.</p><a href="#">Read more</a></article>
    <article class="card"><div class="photo" role="img" aria-label="Photo of a group therapy conversation" style="background:linear-gradient(135deg,#e4dad0,#8c6f5c)"></div><h3>HAVE THE NEED TO TALK BUT UNSURE WHO TO TURN TO?</h3><p>Therapy can assist you in overcoming all of these challenges. Assist you in uncovering the difficulties.</p><a href="#">Read more</a></article>
  </div>
</section>

<footer class="footer">
  <div class="col f-brand"><div class="mark"></div><div class="name">Meadowgate Counselors</div><p>Therapy can assist you in overcoming all of these challenges. Assist you in uncovering the difficulties and barriers that hold you back.</p></div>
  <div class="col f-news"><h4>NEWSLETTER SUBSCRIPTION</h4><p>Receive news, tips and event updates from our practice straight to your inbox.</p><div class="input">Your email</div><br><span class="btn">SUBSCRIBE</span></div>
  <div class="col f-contact"><h4>CONTACT US</h4>
    <ul>
      <li><svg width="12" height="14" viewBox="0 0 12 14"><path d="M6 0a5 5 0 0 0-5 5c0 4 5 9 5 9s5-5 5-9a5 5 0 0 0-5-5z" fill="#fff"/></svg><span>1450 Alder Street, Riverside, CA 92501<br>Mon – Fri, 9am – 6pm</span></li>
      <li><svg width="12" height="12" viewBox="0 0 12 12"><path d="M2 0l3 3-2 2c1 2 2 3 4 4l2-2 3 3-2 2C5 12 0 7 0 2z" fill="#fff"/></svg><span>(951)555-0182</span></li>
      <li><svg width="12" height="10" viewBox="0 0 12 10"><rect width="12" height="10" fill="#fff"/><path d="M0 0l6 5 6-5" fill="none" stroke="#b9cf5c"/></svg><span>marisel582@postbox.example</span></li>
    </ul>
  </div>
  <div class="copyright">Copyright © 2016 Meadowgate Counselors. All Rights Reserved.</div>
</footer>
</body>
</html>
```